Billboard Design for Modern Dispensary

Hello!
We need a eye-catching 12' x 24' billboard designed for a very successful, modern cannabis dispensary on the Oregon coast, United States. Because of rules, we cannot have any marijuana leafs or other cannabis related images (flower, joints, smoke, etc). We can use the words "Shop" or "Dispensary" - we cannot use the words "cannabis", "marijuana".

Some ideas we had are 3 words stacked on left or center of billboard - maybe across bottom we have horizontal logo and the following words - “South of bridge in Marlow Cove”
Another idea is to have a small bubble in bottom/top corner with image of our dog (face only) - with some words around it - like "BONUS Shop Dog" or "Cute Shop Dog" or "Best Shop Dog" or "Friendly Staff"

here's some 3 word examples:
ENJOY
YOUR
TRIP

or

FEEL
GOOD
JUST
AHEAD

or

GOOD
VIBES
ONLY

or

GOOD
TIMES
CHILL
VIBES

I have attached our logo. I have also included a stacked logo version (vertical, not horizontal). the formats are .EPS and .PDF - the logos were created in Affinity Design 2.x.

Our website is lunarwharf.com if you want to see more images, etc about our dispensary.

Artwork Requirements:
The billboard is 12' tall x 25' wide
The artwork needs to be 1”=1’ @ 300dpi
Please add 6” of bleed all around so your total artwork is 13”x26”
Final deliverable should be .Ai file.

Font styles to use
Sans Serif

Colors
0054AA
0677BA
7BADD7
CADEEF
E8F1F8

Requirements
Nice to have
• See the project description - we included some ideas to consider.
Should not have
• No cannabis images, like flower, cannabis leaves, paraphenlia, cartridges, joints, etc.

```html
<!DOCTYPE html>
<html lang="en">
<head>
<meta charset="utf-8">
<title>Sleep Better Tonight – Billboard</title>
<link href="https://fonts.googleapis.com/css2?family=League+Spartan:wght@500;700;800&display=swap" rel="stylesheet">
<style>
  :root {
    --page-bg: #c4c4c4;
    --sky-blue: #3a90cd;
    --ink: #000000;
    --paper: #ffffff;
  }
  html, body {
    margin: 0;
    width: 942px;
    height: 1200px;
    overflow: hidden;
    background: var(--page-bg);
  }
  .billboard {
    position: absolute;
    left: 31px;
    top: 380px;
    width: 1172px;
    height: 586px;
    transform: scale(0.75);
    transform-origin: top left;
    background: var(--sky-blue);
    box-shadow: 10px 14px 18px rgba(0,0,0,0.35);
    overflow: hidden;
    font-family: "League Spartan", sans-serif;
  }
  .billboard__shade {
    position: absolute;
    inset: 0;
  }
  .headline {
    position: absolute;
    left: 76px;
    margin: 0;
    font-weight: 800;
    line-height: 1;
    white-space: nowrap;
  }
  .headline--sleep { top: 58px; font-size: 112px; color: var(--paper); letter-spacing: -3px; }
  .headline--better { top: 150px; font-size: 222px; color: var(--paper); letter-spacing: -6px; }
  .headline--tonight { top: 326px; font-size: 118px; color: var(--sky-blue); letter-spacing: -3px; }

  .location {
    position: absolute;
    right: 84px;
    top: 198px;
    text-align: right;
    color: var(--paper);
    font-weight: 700;
    font-size: 32px;
    line-height: 1.05;
  }
  .location__pin {
    display: block;
    margin: 0 0 10px auto;
    width: 40px;
    height: 48px;
  }

  .contact {
    position: absolute;
    left: 78px;
    top: 478px;
    display: flex;
    align-items: center;
    font-weight: 800;
  }
  .contact__label { color: var(--sky-blue); font-size: 56px; letter-spacing: 1px; }
  .contact__icon { width: 46px; height: 46px; margin: 0 16px 6px 22px; }
  .contact__number { color: var(--paper); font-size: 58px; letter-spacing: -1px; }

  .brand {
    position: absolute;
    left: 788px;
    top: 458px;
    display: flex;
    align-items: center;
    gap: 12px;
  }
  .brand__mark {
    width: 70px;
    height: 70px;
    border-radius: 50%;
    border: 4px solid var(--sky-blue);
    box-sizing: border-box;
  }
  .brand__name {
    color: var(--sky-blue);
    font-weight: 500;
    font-size: 38px;
    white-space: nowrap;
  }
</style>
</head>
<body>
  <section class="billboard" aria-label="Sleep Better Tonight billboard for Lunar Wharf">
    <svg class="billboard__shade" viewBox="0 0 1172 586" aria-hidden="true">
      <path fill="#000" d="M0,150 L88,62 L392,62 L300,154 L690,154 L828,312 L748,392
        q7,-9 14,0 t14,0 t14,0 t14,0 t14,0 t14,0 t14,0 t14,0 t14,0 t14,0
        t14,0 t14,0 t14,0 t14,0 t14,0 t14,0 t14,0 t14,0 t14,0 t14,0
        t14,0 t14,0 t14,0 t14,0 t14,0 t14,0 t14,0 t14,0 t14,0 t14,0 t14,0
        L1172,392 L1172,586 L0,586 Z"/>
    </svg>

    <h1 class="headline headline--sleep">SLEEP</h1>
    <p class="headline headline--better">BETTER</p>
    <p class="headline headline--tonight">TONIGHT</p>

    <div class="location">
      <svg class="location__pin" viewBox="0 0 40 48" aria-hidden="true">
        <ellipse cx="20" cy="42" rx="16" ry="5" fill="none" stroke="#000" stroke-width="3"/>
        <path fill="#000" d="M20,2 C10,2 4,9 4,17 C4,27 20,42 20,42 C20,42 36,27 36,17 C36,9 30,2 20,2 Z"/>
        <circle cx="20" cy="17" r="6" fill="#3a90cd"/>
      </svg>
      SOUTH OF<br>BRIDGE IN<br>MARLOW COVE
    </div>

    <div class="contact">
      <span class="contact__label">CALL US</span>
      <svg class="contact__icon" viewBox="0 0 46 46" aria-hidden="true">
        <circle cx="23" cy="23" r="23" fill="#3a90cd"/>
        <path fill="#000" d="M15,12 l5,-1 l3,7 l-3,3 c2,4 4,6 8,8 l3,-3 l7,3 l-1,5 c-1,2 -3,3 -5,3 c-10,-1 -19,-10 -20,-20 c0,-2 1,-4 3,-5 Z"/>
      </svg>
      <span class="contact__number">541-555-0142</span>
    </div>

    <div class="brand">
      <span class="brand__mark" aria-hidden="true"></span>
      <span class="brand__name">LUNAR WHARF</span>
    </div>
  </section>
</body>
</html>
```